Packaging & Label Design for CDB Products

We are a European CBD company specialising in athletic recovery, sleep improvement and wellness.

We would like the packaging to incorporate our logo and name (and font 'Codec') 'Meridell CBD'. The design must be transferable to all of our products. CBD Oils, Balms, Lip Balm and Vape E-Liquid.

We would like it to be simple but eye-catching and modern. We don't want bright colours. Preferred pallet of muted greys, blacks, white and pastel colours. Geometric concepts, possibly using different colours for each item of the range, we are open to new and fresh ideas (we are seeking you for your experience) and when we find the right design we would likely throw more work in your direction..

Our product range is not complete so the designer must be flexible with some changes and provide files where format can be easily edited by packaging manufacturer. We are also waiting for dimensions for the labels and boxes for several products and will supply the designer with full dimensions of all products once selected.

Oil Box: 2.6 x 9.0 x 2.6 cm (open format 16.7 x 11.6cm)
Labels: 7.8 x 3.3 cm (Front and Back)

Our expected product range will be:
CBD Oil 1000mg
CBD Oil 3000mg
CBD Balm 100mg
CBD Balm 300mg
E-Liquid 500mg
Lip Balm 50mg

We look forward to seeing your ideas.

Best Regards
Meridell CBD

```html
<!DOCTYPE html>
<html lang="en">
<head>
<meta charset="utf-8">
<title>Meridell CBD – Oil Packaging</title>
<link href="https://fonts.googleapis.com/css2?family=Poppins:wght@300;400;600;800&display=swap" rel="stylesheet">
<style>
  :root {
    --stage: #cfcfcf;
    --navy: #252443;
    --sand-light: #dccab4;
    --sand-dark: #c2b4a0;
    --white: #ffffff;
    --ink: #252443;
  }
  html, body {
    margin: 0;
    padding: 0;
    width: 1200px;
    height: 1200px;
    overflow: hidden;
    background: var(--stage);
    font-family: "Poppins", sans-serif;
  }
  .canvas {
    position: relative;
    width: 1200px;
    height: 1200px;
  }
  .panel {
    position: absolute;
    display: flex;
    flex-direction: column;
    box-shadow: 0 18px 40px rgba(0,0,0,0.12);
  }
  .panel__top {
    background: var(--navy);
    display: flex;
    align-items: center;
    justify-content: center;
  }
  .panel__bottom {
    background: linear-gradient(135deg, var(--sand-dark), var(--sand-light));
    display: flex;
    flex-direction: column;
    align-items: center;
    color: var(--ink);
  }
  .brand-name {
    color: var(--white);
    font-weight: 600;
    letter-spacing: 0.06em;
    text-transform: uppercase;
    text-align: center;
    line-height: 1.15;
  }
  .tagline {
    font-weight: 300;
    letter-spacing: 0.22em;
    text-transform: uppercase;
  }
  .product-name {
    font-weight: 800;
    line-height: 1;
  }
  .process {
    font-weight: 400;
    letter-spacing: 0.2em;
    text-transform: uppercase;
  }
  .strength {
    font-weight: 600;
    margin-top: auto;
  }

  /* Box front panel */
  .box-front { left: 230px; top: 200px; width: 420px; height: 800px; }
  .box-front .panel__top { height: 440px; }
  .box-front .panel__bottom { flex: 1; padding: 60px 0 44px; }
  .box-front .brand-name { font-size: 40px; }
  .box-front .tagline { font-size: 15px; }
  .box-front .product-name { font-size: 64px; margin-top: 66px; }
  .box-front .process { font-size: 12px; margin-top: 6px; }
  .box-front .strength { font-size: 15px; }

  /* Bottle label */
  .bottle-label { left: 730px; top: 520px; width: 260px; height: 480px; }
  .bottle-label .panel__top { height: 250px; }
  .bottle-label .panel__bottom { flex: 1; padding: 30px 0 30px; }
  .bottle-label .brand-name { font-size: 26px; }
  .bottle-label .tagline { font-size: 12px; }
  .bottle-label .product-name { font-size: 44px; margin-top: 10px; }
  .bottle-label .process { font-size: 10px; margin-top: 6px; }
  .bottle-label .strength { font-size: 13px; }
</style>
</head>
<body>
  <main class="canvas">
    <section class="panel box-front" aria-label="Oil box front panel">
      <div class="panel__top">
        <div class="brand-name">Meridell CBD</div>
      </div>
      <div class="panel__bottom">
        <div class="tagline">- All Natural -</div>
        <div class="product-name">CBD Oil</div>
        <div class="process">Cold Pressed</div>
        <div class="strength">1000mg</div>
      </div>
    </section>

    <section class="panel bottle-label" aria-label="Bottle front label">
      <div class="panel__top">
        <div class="brand-name">Meridell CBD</div>
      </div>
      <div class="panel__bottom">
        <div class="tagline">- All Natural -</div>
        <div class="product-name">CBD Oil</div>
        <div class="process">Cold Pressed</div>
        <div class="strength">1000mg</div>
      </div>
    </section>
  </main>
</body>
</html>
```